Quarrytide
Quarrytide - Financial Services
Financial Services
www.quarrytidepay.com
Our team has been providing solutions for workers compensation for business owners for over 22 years, our service is provoided at no charge (as it is paid for by the vendor). What makes us unique is our ability to write just about every size company (3 man to 1000) and industry in every state,. Our programs simlyfy the business owners way of doing business by eliminationg several annoying functions that business owners face. For example, with our program a business owner would write one check for payroll, that check would cover his payroll, workers compensation, payroll taxes, employee deductions and garnishments, direct deposit and benefit deductions, year end W-2's and the liabilities that come with year end W-2's. Our program we keeps business owners compliant by keeping them informed about new requirements, labor laws, we provide all employee applications, safety posters, they are able to call with any employee related questions about hiring and firing and so on. All usually for less that they can do it themselves.
Busy, wordy
Service Oriented
White/possible grey, logo colors
Blues and whites and greys, logo colors
left side
We have a content writer completing the text, our home page will contain very little text and focus more as a landing page. The site itself needs to be very clean, simple and easy to navigate but will also allow viewers to go deep into the site if they want to find information, yet at the same time it will not force people away because of too much content

```html
<!DOCTYPE html>
<html lang="en">
<head>
<meta charset="utf-8">
<title>Quarrytide - Financial Services</title>
<link href="https://fonts.googleapis.com/css2?family=Arimo:wght@400;700&family=Open+Sans:wght@400;600;700&display=swap" rel="stylesheet">
<style>
:root{
  --blue:#1a6fc4;
  --blue-dark:#0b3f86;
  --blue-deep:#062a63;
  --blue-light:#3f95e6;
  --ink:#333;
  --grey-text:#555;
  --footer:#262626;
  --footer-text:#bdbdbd;
  --white:#fff;
}
*{margin:0;padding:0;box-sizing:border-box}
html,body{width:1200px;height:965px;overflow:hidden}
body{font-family:"Arimo",Arial,sans-serif;color:var(--ink);background:var(--white);position:relative}

.site-header{position:absolute;left:0;top:0;width:1200px;height:110px;background:linear-gradient(#fff,#f4f4f4);border-top:4px solid var(--blue-dark)}
.brand{position:absolute;left:170px;top:22px;display:flex;align-items:center;gap:16px}
.brand-mark{width:60px;height:60px;border-radius:50%;background:var(--blue)}
.brand-name{font-family:"Open Sans",sans-serif;font-weight:700;font-size:40px;color:var(--blue-dark);letter-spacing:1px}
.contact{position:absolute;right:155px;top:26px;text-align:right}
.contact-label{font-size:13px;color:var(--grey-text)}
.contact-phone{display:flex;align-items:center;gap:10px;font-family:"Open Sans",sans-serif;font-weight:700;font-size:32px;color:var(--blue);line-height:1.1}

.main-nav{position:absolute;left:0;top:110px;width:1200px;height:52px;background:linear-gradient(#fafafa,#e4e4e4);border-top:1px solid #ccc;border-bottom:1px solid #c4c4c4}
.main-nav ul{list-style:none;display:flex;position:absolute;left:160px;top:10px}
.main-nav li a{display:block;padding:0 24px;height:32px;line-height:32px;font-size:17px;color:#222;text-decoration:none;border-radius:4px}
.main-nav li:nth-child(1) a{padding-left:22px}
.main-nav li a.active{background:var(--blue);color:var(--white);width:130px;text-align:center}

.hero-zone{position:absolute;left:0;top:163px;width:1200px;height:360px;background:linear-gradient(#9c9c9c,#d4d4d4 45%,#f3f3f3)}
.hero{position:absolute;left:149px;top:28px;width:902px;height:300px;border-radius:10px;border:3px solid var(--blue-dark);overflow:hidden}
.hero-backdrop{position:absolute;inset:0;background:radial-gradient(ellipse at 35% 55%,#3d8fe0,#1462b8 55%,#0a3e86)}
.hero-text{position:absolute;left:30px;top:76px;font-family:"Open Sans",sans-serif;color:var(--white);font-size:25px;line-height:32px;text-shadow:0 1px 2px rgba(0,0,0,.3)}
.hero-text strong{display:block;font-size:38px;line-height:48px;font-weight:600}
.hero-links{position:absolute;left:555px;top:55px;list-style:none}
.hero-links li{width:319px;height:52px;margin-bottom:13px;background:rgba(255,255,255,.18);border:1px solid rgba(255,255,255,.35);display:flex;align-items:center;gap:12px;padding-left:16px;font-family:"Open Sans",sans-serif;font-size:23px;color:var(--white)}
.hero-links .dot{width:22px;height:22px;border-radius:50%;border:3px solid var(--white)}

.welcome{position:absolute;left:149px;top:536px;width:590px}
.section-title{display:flex;align-items:center;gap:12px;font-family:"Open Sans",sans-serif;font-size:25px;font-weight:600;color:#222;margin-bottom:18px}
.section-title .accent{color:var(--blue-dark)}
.title-icon{width:36px;height:36px;border-radius:50%;background:var(--blue)}
.welcome p{font-size:11.5px;line-height:15px;color:var(--grey-text);margin-bottom:12px}
.btn-more{display:inline-block;height:26px;line-height:26px;padding:0 34px 0 14px;border-radius:13px;background:linear-gradient(#3a86d6,var(--blue-dark));color:var(--white);font-size:12px;font-weight:700;position:relative;text-decoration:none}
.btn-more::after{content:"";position:absolute;right:10px;top:7px;width:12px;height:12px;border-radius:50%;background:var(--white)}

.news{position:absolute;left:792px;top:536px;width:259px}
.news .section-title{font-size:21px;margin-bottom:14px}
.news .title-icon{width:30px;height:30px}
.news-item{display:flex;gap:12px;padding:10px 0 12px;border-top:1px solid #ddd}
.news-item:last-of-type{border-bottom:1px solid #ddd;margin-bottom:14px}
.news-date{font-size:12px;font-weight:700;color:var(--blue-dark);margin-bottom:4px}
.news-body{font-size:11px;line-height:14px;color:var(--grey-text)}

.site-footer{position:absolute;left:0;top:815px;width:1200px;height:150px;background:var(--footer);border-top:4px solid #111}
.footer-nav{position:absolute;left:157px;top:38px;list-style:none;display:flex;font-size:12px;color:var(--footer-text)}
.footer-nav li{padding:0 12px;border-left:1px solid #777}
.footer-nav li:first-child{padding-left:0;border-left:none}
.copyright{position:absolute;left:157px;top:68px;font-size:13px;color:var(--footer-text)}
.follow{position:absolute;left:876px;top:36px;display:flex;align-items:center;gap:10px;color:var(--white);font-size:15px;font-weight:700}
.follow .social{width:24px;height:24px;border-radius:50%;background:#555}
.footer-brand{position:absolute;left:884px;top:82px;display:flex;align-items:center;gap:10px}
.footer-brand .mark{width:36px;height:36px;border-radius:50%;background:#777}
.footer-brand .name{font-family:"Open Sans",sans-serif;font-size:24px;font-weight:700;color:#8a8a8a}
</style>
</head>
<body>

<header class="site-header">
  <div class="brand">
    <div class="brand-mark"></div>
    <span class="brand-name">QUARRYTIDE</span>
  </div>
  <div class="contact">
    <div class="contact-label">Call Us for Financial Support</div>
    <div class="contact-phone">
      <svg width="30" height="30" viewBox="0 0 30 30" aria-hidden="true">
        <rect x="1" y="3" width="28" height="24" rx="5" fill="#1a6fc4"/>
        <path d="M8 19c0-6 3-9 7-9s7 3 7 9z" fill="#fff"/>
        <rect x="7" y="8" width="16" height="4" rx="2" fill="#fff"/>
      </svg>
      866-555-0142
    </div>
  </div>
</header>

<nav class="main-nav">
  <ul>
    <li><a href="#">Home</a></li>
    <li><a href="#" class="active">About Us</a></li>
    <li><a href="#">Products</a></li>
    <li><a href="#">Services</a></li>
    <li><a href="#">Solution</a></li>
    <li><a href="#">Careers</a></li>
    <li><a href="#">Contact us</a></li>
  </ul>
</nav>

<section class="hero-zone">
  <div class="hero">
    <div class="hero-backdrop" role="img" aria-label="Blue abstract banner artwork behind the headline"></div>
    <div class="hero-text">
      Our team has been providing solutions<br>
      for workers Compensation for business
      <strong>owners for over 22 years</strong>
    </div>
    <ul class="hero-links">
      <li><span class="dot"></span>Term Loans</li>
      <li><span class="dot"></span>Installment Loans</li>
      <li><span class="dot"></span>Payroll &amp; Debit Cards</li>
    </ul>
  </div>
</section>

<section class="welcome">
  <h2 class="section-title"><span class="title-icon"></span>Welcome to <span class="accent">Quarrytide</span></h2>
  <p>Lorem Ipsum is simply dummy text of the printing and typesetting industry. Lorem Ipsum has been the industry's standard dummy text ever since the 1500s, when an unknown printer took a galley of type and scrambled it to make a type specimen book. It has survived not only five centuries, but also the leap into electronic typesetting, remaining essentially unchanged. It was popularised in the 1960s with the release of Letraset sheets containing Lorem Ipsum passages, and more recently with desktop publishing software like Aldus PageMaker including versions of Lorem Ipsum.</p>
  <p>Lorem Ipsum is simply dummy text of the printing and typesetting industry. Lorem Ipsum has been the industry's standard dummy text ever since the 1500s, when an unknown printer took a galley of type and scrambled it to make a type specimen book.</p>
  <a href="#" class="btn-more">Read More</a>
</section>

<aside class="news">
  <h2 class="section-title"><span class="title-icon"></span>Latest News</h2>
  <div class="news-item">
    <svg width="44" height="44" viewBox="0 0 44 44" aria-hidden="true">
      <rect x="2" y="6" width="40" height="36" rx="3" fill="#fff" stroke="#999"/>
      <rect x="2" y="6" width="40" height="11" rx="3" fill="#1a6fc4"/>
      <text x="22" y="36" text-anchor="middle" font-family="Arimo,sans-serif" font-size="16" font-weight="700" fill="#333">14</text>
    </svg>
    <div>
      <div class="news-date">September 2011</div>
      <div class="news-body">Lorem ipsum dolor sit amet, consectetur adipiscing elit sed do eiusmod.</div>
    </div>
  </div>
  <div class="news-item">
    <svg width="44" height="44" viewBox="0 0 44 44" aria-hidden="true">
      <rect x="2" y="6" width="40" height="36" rx="3" fill="#fff" stroke="#999"/>
      <rect x="2" y="6" width="40" height="11" rx="3" fill="#1a6fc4"/>
      <text x="22" y="36" text-anchor="middle" font-family="Arimo,sans-serif" font-size="16" font-weight="700" fill="#333">14</text>
    </svg>
    <div>
      <div class="news-date">September 2011</div>
      <div class="news-body">Lorem ipsum dolor sit amet, consectetur adipiscing elit sed do eiusmod.</div>
    </div>
  </div>
  <a href="#" class="btn-more">Read More</a>
</aside>

<footer class="site-footer">
  <ul class="footer-nav">
    <li>HOME</li>
    <li>ABOUT US</li>
    <li>PRODUCTS &amp; SERVICES</li>
    <li>SOLUTION</li>
    <li>CAREERS</li>
    <li>CONTACT US</li>
  </ul>
  <div class="copyright">© 2011Quarrytide.com. All rights reserved.</div>
  <div class="follow">Follow Us
    <span class="social"></span><span class="social"></span><span class="social"></span><span class="social"></span>
  </div>
  <div class="footer-brand">
    <span class="mark"></span>
    <span class="name">QUARRYTIDE</span>
  </div>
</footer>

</body>
</html>
```